Business Card Design Project

I need a cool business card design for the company that will build residential houses.
The card should include:
1) Name: Borek Valdisov
2) Cell: 587.244.XXXX
3) Email: bor.valdisov@qorvina.example
4) Position: General Manager
5) Residential Home Building
6) Company logo that I have uploaded

Industry/Entity Type

Residential

```html
<!DOCTYPE html>
<html lang="en">
<head>
<meta charset="utf-8">
<title>Halvern Developments – Business Card</title>
<link rel="stylesheet" href="https://fonts.googleapis.com/css2?family=Open+Sans:wght@400;600;700&display=swap">
<style>
  :root {
    --backdrop: #e8e4df;
    --card: #ffffff;
    --brand-blue: #1f4e9c;
    --brand-green: #5cb43a;
    --text-grey: #6f6f6f;
    --rule-grey: #c4c4c4;
  }
  * { box-sizing: border-box; margin: 0; padding: 0; }
  html, body {
    width: 1200px; height: 836px; overflow: hidden;
    background: var(--backdrop);
    font-family: "Open Sans", Arial, sans-serif;
  }
  .canvas { position: relative; width: 1200px; height: 836px; }
  .card {
    position: absolute; left: 320px; width: 560px; height: 320px;
    background: var(--card); border-radius: 16px; overflow: hidden;
    box-shadow: 0 6px 18px rgba(0,0,0,.18);
  }
  .card--front { top: 78px; }
  .card--back { top: 438px; }

  .brand { display: flex; align-items: center; gap: 10px; }
  .brand__dot { width: 18px; height: 18px; border-radius: 50%; background: var(--brand-green); }
  .brand__name { color: var(--brand-blue); font-weight: 700; font-size: 24px; letter-spacing: .5px; line-height: 1; }

  .card--front .brand { position: absolute; left: 42px; top: 52px; }
  .tagline {
    position: absolute; left: 42px; top: 92px;
    color: var(--brand-green); font-size: 15px; font-weight: 600;
  }
  .person { position: absolute; left: 50px; top: 200px; }
  .person__name { color: var(--brand-blue); font-size: 14px; font-weight: 600; }
  .person__role { color: var(--text-grey); font-size: 13px; margin-top: 2px; }

  .divider {
    position: absolute; left: 300px; top: 160px; width: 1px; height: 50px;
    background: var(--rule-grey);
  }
  .contact { position: absolute; left: 330px; top: 150px; list-style: none; }
  .contact__item {
    display: flex; align-items: center; gap: 8px;
    color: var(--text-grey); font-size: 12.5px; line-height: 20px;
  }
  .contact__icon { width: 12px; height: 12px; flex: none; }

  .wave { position: absolute; left: 0; bottom: 0; width: 560px; height: 320px; }

  .card--back .brand {
    position: absolute; left: 0; right: 0; top: 130px; justify-content: center;
  }
  .card--back .brand__name { font-size: 28px; }
  .website {
    position: absolute; left: 0; right: 0; bottom: 28px; text-align: center;
    color: var(--brand-blue); font-size: 14px; font-weight: 600;
  }
</style>
</head>
<body>
<main class="canvas">
  <section class="card card--front" aria-label="Business card front">
    <svg class="wave" viewBox="0 0 560 320" aria-hidden="true">
      <path d="M0,320 L0,308 C170,304 370,270 560,196 L560,320 Z" fill="var(--brand-blue)"/>
      <path d="M0,296 C190,296 380,252 545,190" fill="none" stroke="var(--brand-green)" stroke-width="9"/>
    </svg>

    <div class="brand">
      <span class="brand__dot"></span>
      <span class="brand__name">Halvern Developments</span>
    </div>
    <p class="tagline">Residential Home Building</p>

    <div class="person">
      <p class="person__name">Borek Valdisov</p>
      <p class="person__role">General Manager</p>
    </div>

    <span class="divider"></span>

    <ul class="contact">
      <li class="contact__item">
        <svg class="contact__icon" viewBox="0 0 12 12" aria-hidden="true">
          <rect x="3" y="0.5" width="6" height="11" rx="1.2" fill="none" stroke="var(--brand-blue)" stroke-width="1.3"/>
          <rect x="5" y="9" width="2" height="1" fill="var(--brand-blue)"/>
        </svg>
        587.244.XXXX
      </li>
      <li class="contact__item">
        <svg class="contact__icon" viewBox="0 0 12 12" aria-hidden="true">
          <rect x="0.6" y="2.2" width="10.8" height="7.6" fill="none" stroke="var(--brand-blue)" stroke-width="1.2"/>
          <path d="M0.6,2.4 L6,6.8 L11.4,2.4" fill="none" stroke="var(--brand-blue)" stroke-width="1.2"/>
        </svg>
        bor.valdisov@qorvina.example
      </li>
    </ul>
  </section>

  <section class="card card--back" aria-label="Business card back">
    <div class="brand">
      <span class="brand__dot"></span>
      <span class="brand__name">Halvern Developments</span>
    </div>
    <p class="website">www.halverndevelopments.example</p>
  </section>
</main>
</body>
</html>
```